Brookside Grocer

Hope all is well!

Wanted to make business cards for my father. His name is Faisal Qureshi and owns convenience stores. I have attached logo :)

He does not want any title just simple name and phone. An email would be nice as well.

Faisal Qureshi
Cell: 413-585-2046
Store: 413-719-4820

Brooksidegrocer512@fernpost.com

The design and style is totally up to you :) The colors we were looking for were the same as logo :)

```html
<!DOCTYPE html>
<html lang="en">
<head>
<meta charset="utf-8">
<title>Brookside Grocer — Business Card</title>
<link rel="stylesheet" href="https://fonts.googleapis.com/css2?family=Tinos:wght@700&family=Mulish:wght@500&display=swap">
<style>
  :root {
    --backdrop: #d3d4d6;
    --navy: #283a78;
    --navy-deep: #243570;
    --red: #ec2f37;
    --paper: #ffffff;
  }
  * { margin: 0; padding: 0; box-sizing: border-box; }
  html, body {
    width: 900px; height: 1200px; overflow: hidden;
    background: var(--backdrop);
  }
  .canvas { position: relative; width: 900px; height: 1200px; }
  .card { position: absolute; width: 633px; height: 364px; }
  .card-front {
    left: 133px; top: 210px;
    background: linear-gradient(135deg, var(--navy-deep), var(--navy));
    display: flex; align-items: center; justify-content: center;
  }
  .card-back { left: 134px; top: 624px; background: var(--paper); }
  .brand-name {
    font-family: "Tinos", serif; font-weight: 700;
    text-transform: uppercase; white-space: nowrap; letter-spacing: 0.5px;
  }
  .card-front .brand-name { color: var(--paper); font-size: 40px; }
  .card-back .brand-name {
    position: absolute; left: 0; right: 0; top: 62px;
    text-align: center; color: var(--navy); font-size: 29px;
  }
  .contact-block { position: absolute; left: 186px; top: 182px; width: 262px; }
  .person-name {
    font-family: "Tinos", serif; font-weight: 700; font-size: 26px;
    color: var(--navy); text-transform: uppercase; white-space: nowrap;
    letter-spacing: 0.3px;
  }
  .rule { display: block; margin-top: 10px; }
  .contact-list { list-style: none; margin-top: 12px; font-family: "Mulish", sans-serif; font-weight: 500; color: var(--navy); }
  .contact-list li { height: 26px; line-height: 26px; white-space: nowrap; }
  .contact-list .label { color: var(--red); }
  .phone { font-size: 19px; letter-spacing: 2.4px; }
  .email { font-size: 13.5px; }
</style>
</head>
<body>
<main class="canvas">
  <section class="card card-front">
    <h1 class="brand-name">Brookside Grocer</h1>
  </section>

  <section class="card card-back">
    <p class="brand-name">Brookside Grocer</p>
    <div class="contact-block">
      <h2 class="person-name">Faisal Qureshi</h2>
      <svg class="rule" width="262" height="14" viewBox="0 0 262 14" aria-hidden="true">
        <rect x="0" y="0" width="262" height="3" fill="var(--red)"/>
        <rect x="0" y="5.5" width="262" height="3" fill="var(--red)"/>
        <rect x="0" y="11" width="262" height="3" fill="var(--red)"/>
      </svg>
      <ul class="contact-list">
        <li class="phone"><span class="label">C:</span>413-585-2046</li>
        <li class="phone"><span class="label">S:</span>413-719-4820</li>
        <li class="email"><span class="label">E:</span> Brooksidegrocer512@fernpost.com</li>
      </ul>
    </div>
  </section>
</main>
</body>
</html>
```